Law Firm Business Card

This is a business card for a law firm that serves US military and veterans.

The card must have ONLY the following (we want an uncluttered look):

- Company logo (PNG, GIF, JPEG copies uploaded)
- A tagline reading: "a law firm for service members and veterans"
- My name and title: "Martin Okello" and "Attorney"
- My email: "martin.okello@harborlinecounsel.com"
- My number: "855-FILE-NOW (345-3669)"

We are looking for a clean, simple layout with only the above information, likely printed on a bright white cotton stock. The font of our logo is DIN 1451, and the font used on our website is Helvetica Neue. The color of our logo is #336699, and we probably want the tagline in that color also, and my contact information in a dark grey. Please review our website at www.harborlinecounsel.com to ensure your card design complements our website style.

Thanks and we look forward to seeing your submissions.

A few notes:

- Two-sided submissions are ok
- Please don't add graphics (scales of justice, judges hammer, etc)

```html
<!DOCTYPE html>
<html lang="en">
<head>
<meta charset="utf-8">
<title>Harborline Counsel – Business Card</title>
<link rel="stylesheet" href="https://fonts.googleapis.com/css2?family=Barlow+Condensed:wght@600&family=Crimson+Text:ital,wght@0,400;1,400&display=swap">
<style>
  :root {
    --brand-blue: #336699;
    --card-blue: #2f69c6;
    --logo-blue: #3b6cc2;
    --ink-dark: #2b2b2b;
    --band-grey: #6f7675;
    --paper: #ffffff;
    --backdrop: #4a3428;
  }
  * { margin: 0; padding: 0; box-sizing: border-box; }
  html, body {
    width: 1200px;
    height: 501px;
    overflow: hidden;
    background: var(--backdrop);
  }
  .stage {
    position: relative;
    width: 1200px;
    height: 501px;
  }
  .card {
    position: absolute;
    top: 105px;
    width: 500px;
    height: 290px;
    overflow: hidden;
    box-shadow: 0 6px 18px rgba(0,0,0,0.35);
  }
  /* Front */
  .card-front {
    left: 70px;
    background: var(--paper);
  }
  .front-wordmark {
    position: absolute;
    top: 34px;
    left: 0;
    width: 100%;
    text-align: center;
    font-family: "Barlow Condensed", sans-serif;
    font-weight: 600;
    font-size: 44px;
    letter-spacing: 1px;
    line-height: 1;
    color: var(--logo-blue);
  }
  .identity {
    position: absolute;
    top: 150px;
    left: 60px;
    width: 132px;
    text-align: right;
    font-family: "Crimson Text", serif;
    color: var(--ink-dark);
  }
  .identity-name { font-size: 19px; line-height: 1.1; }
  .identity-title { font-size: 13px; line-height: 1.2; }
  .divider {
    position: absolute;
    top: 138px;
    left: 204px;
    width: 1px;
    height: 54px;
    background: var(--brand-blue);
  }
  .contacts {
    position: absolute;
    top: 140px;
    left: 214px;
    list-style: none;
    font-family: "Crimson Text", serif;
    color: var(--ink-dark);
  }
  .contact-item {
    display: flex;
    align-items: center;
    gap: 6px;
    height: 24px;
  }
  .contact-phone { font-size: 14px; }
  .contact-email { font-size: 12px; }
  .contact-icon { width: 11px; height: 11px; flex: none; }
  .front-band {
    position: absolute;
    left: 0;
    bottom: 0;
    width: 500px;
    height: 40px;
  }
  .front-tagline {
    position: absolute;
    left: 0;
    width: 100%;
    text-align: center;
    bottom: 44px;
    font-family: "Crimson Text", serif;
    font-size: 15px;
    line-height: 1;
    color: var(--logo-blue);
    white-space: nowrap;
  }
  /* Back */
  .card-back {
    left: 630px;
    background: var(--card-blue);
    color: var(--paper);
  }
  .back-wordmark {
    position: absolute;
    top: 95px;
    left: 34px;
    font-family: "Barlow Condensed", sans-serif;
    font-weight: 600;
    font-size: 44px;
    line-height: 1;
    letter-spacing: 1px;
    color: var(--paper);
  }
  .back-tagline {
    position: absolute;
    top: 70px;
    left: 225px;
    width: 250px;
    text-align: center;
    font-family: "Crimson Text", serif;
    font-size: 24px;
    line-height: 1.15;
  }
  .back-web {
    position: absolute;
    top: 190px;
    left: 225px;
    width: 250px;
    text-align: center;
    font-family: "Crimson Text", serif;
    font-style: italic;
    font-size: 17px;
  }
</style>
</head>
<body>
<main class="stage">
  <section class="card card-front" aria-label="Business card front">
    <div class="front-wordmark">HARBORLINE COUNSEL</div>

    <div class="identity">
      <p class="identity-name">Martin Okello</p>
      <p class="identity-title">Attorney</p>
    </div>
    <div class="divider"></div>
    <ul class="contacts">
      <li class="contact-item contact-phone">
        <svg class="contact-icon" viewBox="0 0 24 24" aria-hidden="true">
          <path fill="#2b2b2b" d="M6.6 10.8c1.4 2.8 3.8 5.1 6.6 6.6l2.2-2.2c.3-.3.7-.4 1-.2 1.1.4 2.3.6 3.6.6.6 0 1 .4 1 1V20c0 .6-.4 1-1 1C10.6 21 3 13.4 3 4c0-.6.4-1 1-1h3.5c.6 0 1 .4 1 1 0 1.2.2 2.4.6 3.6.1.3 0 .7-.2 1z"/>
        </svg>
        <span>855-FILE-NOW (345-3669)</span>
      </li>
      <li class="contact-item contact-email">
        <svg class="contact-icon" viewBox="0 0 24 24" aria-hidden="true">
          <rect x="2" y="5" width="20" height="14" rx="2" fill="#2b2b2b"/>
          <path d="M3 6l9 7 9-7" fill="none" stroke="#fff" stroke-width="1.8"/>
        </svg>
        <span>martin.okello@harborlinecounsel.com</span>
      </li>
    </ul>

    <p class="front-tagline">A Law Firm For Service Members And Veterans</p>
    <svg class="front-band" viewBox="0 0 500 40" aria-hidden="true">
      <polygon points="0,28 262,28 248,40 0,40" fill="#6f7675"/>
      <polygon points="272,28 500,14 500,40 258,40" fill="#3b6cc2"/>
    </svg>
  </section>

  <section class="card card-back" aria-label="Business card back">
    <div class="back-wordmark">HARBORLINE<br>COUNSEL</div>
    <p class="back-tagline">A Law Firm<br>For Service<br>Members &amp; Veterans</p>
    <p class="back-web">www.harborlinecounsel.com</p>
  </section>
</main>
</body>
</html>
```